Amber Lantern Cafe Business Card

We need a business card design for a new European Cafe. Main menu will be coffee and deserts.

Requirements
Must have
• Logo - 1 of the attached versions
Address - TBA (you can use 487 Morrow Ave Unit 9 for now)
Phone - TBA (you can use 555-238-4176 for now)

```html
<!DOCTYPE html>
<html lang="en">
<head>
<meta charset="utf-8">
<title>Amber Lantern Cafe – Business Card</title>
<link rel="stylesheet" href="https://fonts.googleapis.com/css2?family=Open+Sans:wght@400&family=Quicksand:wght@500&display=swap">
<style>
  :root {
    --backdrop: #2e2522;
    --card-top: #4b3b34;
    --card-bottom: #3c2e28;
    --ink: #ffffff;
    --ink-soft: #f1ebe7;
  }
  * { margin: 0; padding: 0; box-sizing: border-box; }
  html, body {
    width: 1200px;
    height: 1000px;
    overflow: hidden;
    background: var(--backdrop);
  }
  .business-card {
    position: absolute;
    left: 100px;
    top: 231px;
    width: 1000px;
    height: 538px;
    background: linear-gradient(180deg, var(--card-top) 0%, var(--card-bottom) 100%);
    box-shadow: 0 6px 18px rgba(0,0,0,0.45);
    color: var(--ink);
  }
  .brand-mark {
    position: absolute;
    left: 405px;
    top: 72px;
    width: 190px;
    height: 180px;
    background: var(--ink);
    border-radius: 12px;
  }
  .brand-name {
    position: absolute;
    left: 0;
    width: 100%;
    top: 272px;
    text-align: center;
    font-family: "Open Sans", sans-serif;
    font-weight: 400;
    font-size: 64px;
    line-height: 1;
    letter-spacing: -0.5px;
    color: var(--ink);
  }
  .brand-subline {
    position: absolute;
    left: 275px;
    width: 450px;
    top: 350px;
    display: flex;
    align-items: center;
    gap: 22px;
    font-family: "Open Sans", sans-serif;
    font-weight: 400;
    font-size: 40px;
    line-height: 1;
    color: var(--ink);
  }
  .brand-subline .rule {
    flex: 1;
    height: 3px;
    background: var(--ink);
  }
  .contact-line {
    position: absolute;
    left: 0;
    width: 100%;
    top: 510px;
    top: 508px;
  }
  .contact-row {
    position: absolute;
    left: 0;
    width: 100%;
    top: 462px;
    display: flex;
    justify-content: center;
    align-items: center;
    gap: 26px;
    font-family: "Quicksand", sans-serif;
    font-weight: 500;
    font-size: 18px;
    color: var(--ink-soft);
  }
  .contact-row .divider {
    width: 7px;
    height: 7px;
    background: var(--ink-soft);
    transform: rotate(45deg);
  }
</style>
</head>
<body>
  <main class="business-card">
    <div class="brand-mark" aria-hidden="true"></div>
    <div class="brand-name">Amber Lantern</div>
    <div class="brand-subline">
      <span class="rule"></span>
      <span>Cafe</span>
      <span class="rule"></span>
    </div>
    <div class="contact-row">
      <span class="address">487 Morrow Ave Unit 9</span>
      <span class="divider" aria-hidden="true"></span>
      <span class="phone">555-238-4176</span>
    </div>
  </main>
</body>
</html>
```